Ridgeline Build Network Inc. Letterhead

Creation of attractive and eye catching letterhead for a business start-up for the construction industry. Letterhead must relate to construction, but avoid standard hammer and tools in the design.
Updates

I forgot to add some details, sorry about that. Some pertinent info: Ph: 541-555-0148 ridgelinebuildnet.example 487 Willowmere Ave, Ste 210 Alderbrook, CA 95699 info@ridgelinebuildnet.example not sure if slogan should be in there" “Uniting Building Specialists To Shape a Stronger, Fairer Trade.” must be able to be used in word. Thanks!

```html
<!DOCTYPE html>
<html lang="en">
<head>
<meta charset="utf-8">
<title>Ridgeline Build Network Inc. Letterhead</title>
<link rel="stylesheet" href="https://fonts.googleapis.com/css2?family=Open+Sans:wght@700&family=Questrial&display=swap">
<style>
  :root {
    --board: #ebe3e3;
    --label: #333333;
    --red: #b91f26;
    --navy: #1f2455;
    --paper: #ffffff;
    --ink: #333333;
  }
  html, body { margin: 0; padding: 0; overflow: hidden; }
  body { width: 1200px; height: 873px; background: var(--board); position: relative; font-family: "Questrial", sans-serif; }
  .board-title, .sheet-label {
    position: absolute; margin: 0; font-family: "Open Sans", sans-serif; font-weight: 700;
    color: var(--label); transform: translateX(-50%); white-space: nowrap; line-height: 1;
  }
  .board-title { left: 615px; top: 30px; font-size: 60px; letter-spacing: -1px; }
  .sheet-label { top: 780px; font-size: 52px; letter-spacing: -1px; }
  .sheet-label--front { left: 326px; }
  .sheet-label--back { left: 829px; }

  .sheet { position: absolute; top: 142px; width: 469px; height: 606px; box-shadow: 0 4px 10px rgba(0,0,0,0.22); }
  .sheet--front { left: 103px; background: var(--paper); border-top: 6px solid var(--navy); box-sizing: border-box; }
  .sheet--back { left: 614px; background: var(--red); }

  .brand-name {
    position: absolute; text-align: center; font-family: "Questrial", sans-serif;
    text-transform: uppercase; letter-spacing: 2px; line-height: 1.25; margin: 0;
  }
  .brand-name--header { left: 27px; top: 60px; width: 190px; font-size: 15px; color: var(--navy); }
  .brand-name--watermark { left: 40px; top: 330px; width: 389px; font-size: 30px; color: var(--navy); opacity: 0.08; }
  .brand-name--back { left: 50px; top: 325px; width: 369px; font-size: 28px; color: #ffffff; }

  .slogan { position: absolute; right: 12px; top: 38px; width: 220px; text-align: center; color: var(--ink); margin: 0; }
  .slogan__lead { display: block; font-size: 13.5px; }
  .slogan__key { display: block; font-size: 32px; color: var(--red); line-height: 1.05; }
  .slogan__tail { display: block; font-size: 11px; }

  .contact-band {
    position: absolute; left: 0; right: 0; bottom: 18px; height: 38px; background: var(--red);
    color: #ffffff; font-size: 10px; text-align: center; box-sizing: border-box; padding-top: 5px;
  }
  .contact-band__row { display: flex; justify-content: center; gap: 22px; margin: 0 0 4px; }
  .contact-band p { margin: 0; }
</style>
</head>
<body>
  <h1 class="board-title">OPTION 01</h1>

  <section class="sheet sheet--front" aria-label="Letterhead front">
    <p class="brand-name brand-name--header">Ridgeline Build Network Inc.</p>
    <p class="slogan">
      <span class="slogan__lead">Uniting Building</span>
      <span class="slogan__key">Specialists</span>
      <span class="slogan__tail">To Shape a Stronger, Fairer Trade.</span>
    </p>
    <p class="brand-name brand-name--watermark">Ridgeline Build Network Inc.</p>
    <footer class="contact-band">
      <div class="contact-band__row">
        <span>541-555-0148</span><span>|</span>
        <span>ridgelinebuildnet.example</span><span>|</span>
        <span>info@ridgelinebuildnet.example</span>
      </div>
      <p>487 Willowmere Ave, Ste 210 Alderbrook CA 95699</p>
    </footer>
  </section>

  <section class="sheet sheet--back" aria-label="Letterhead back">
    <p class="brand-name brand-name--back">Ridgeline Build Network Inc.</p>
  </section>

  <h2 class="sheet-label sheet-label--front">FRONT</h2>
  <h2 class="sheet-label sheet-label--back">BACK</h2>
</body>
</html>
```